Kelvaro.lu - Héritage en confiance

As a rule, most people plan everything meticulously down to the smallest detail, at least when it comes to aspects such as building a house, buying a car, or making major purchases. However, very few think about what is usually the single biggest “transaction” of their entire lives and make provisions for it. We are talking about inheritance – or, from the other perspective, inheriting. In any case, it is about estate planning.

Target Market(s)

Inheritance of a property - People that inheritated a property

Industry/Entity Type

Inheritance of a property - Real Estate

Coding

Coded - Design and coding required

Number of Pages Required

4 page

Font styles to use
Decorative

Colors
0054AA
0677BA
7BADD7
CADEEF
E8F1F8

Requirements
Must have
• Four different Navigation buttons: 1. Immobilier (if somebody inherated a house or flat) 2. Services (if people do not kow what to do) 3. Calculatrice (if people want to get an idea of the value of the house or flat) 4. Contact (to get in touch with us through a text form).
Nice to have
• Since visitors to this site may be in mourning, the website should be very user-friendly and welcoming.
Should not have
• Too bright, too many colors...

```html
<!DOCTYPE html>
<html lang="fr">
<head>
<meta charset="utf-8">
<title>Kelvaro.lu – Héritage en confiance</title>
<link href="https://fonts.googleapis.com/css2?family=Krona+One&family=Roboto:wght@400;500;700&display=swap" rel="stylesheet">
<style>
:root{
  --navy:#0054AA;
  --blue:#0677BA;
  --sky:#7BADD7;
  --mist:#CADEEF;
  --ice:#E8F1F8;
  --ink:#222;
  --grey:#777;
  --white:#fff;
}
*{margin:0;padding:0;box-sizing:border-box}
html,body{width:1200px;height:3995px;overflow:hidden}
body{position:relative;background:var(--white);font-family:'Roboto',sans-serif;color:var(--ink)}
.abs{position:absolute}
.display{font-family:'Krona One',sans-serif;color:var(--navy);text-transform:uppercase;letter-spacing:1px}
.btn{position:absolute;display:flex;align-items:center;justify-content:center;background:var(--blue);color:var(--white);font-weight:700;font-size:17px;border-radius:3px;text-transform:uppercase}
.copy{position:absolute;font-size:17px;line-height:30.5px;color:var(--grey);text-align:justify}
.photo{position:absolute}
/* header */
.topline{top:0;left:0;width:1200px;height:4px;background:var(--blue)}
.header{top:4px;left:0;width:1200px;height:108px;background:var(--white)}
.logo{left:144px;top:40px;font-family:'Krona One',sans-serif;font-size:27px;color:var(--navy);letter-spacing:1px}
.nav a{position:absolute;top:42px;height:34px;line-height:34px;font-size:15px;color:var(--ink);text-decoration:none;text-transform:uppercase}
.nav a.active{background:var(--blue);color:var(--white);padding:0 15px;border-radius:2px}
.search{left:1016px;top:40px;width:38px;height:38px;border-radius:50%;background:var(--sky)}
/* hero */
.hero-title{left:144px;top:258px;font-size:34px;line-height:48px;color:var(--white);letter-spacing:2px}
.field{position:absolute;background:var(--white);border:1px solid #cfd8e0;font-size:16px;color:#555;padding:0 22px;line-height:54px}
.footer-nav{left:0;top:3734px;width:1200px;text-align:center;font-size:19px;font-weight:500;color:var(--white)}
.footer-nav span{margin:0 26px}
.legal{left:0;top:3794px;width:1200px;text-align:center;font-size:14px;color:var(--white)}
.social{top:3860px;width:46px;height:46px;border-radius:50%;background:var(--white);border:2px solid var(--mist)}
</style>
</head>
<body>

<!-- backgrounds -->
<div class="photo" style="left:0;top:112px;width:1200px;height:700px;background:linear-gradient(100deg,#3a3d3a 0%,#5b5a52 40%,#8a7a62 70%,#5c5f66 100%)" role="img" aria-label="Photo d'une signature de document chez le notaire"></div>
<div class="photo" style="left:650px;top:680px;width:550px;height:800px;background:linear-gradient(180deg,rgba(232,241,248,0) 0%,rgba(230,226,216,.55) 40%,rgba(232,241,248,.4) 100%)" role="img" aria-label="Façade d'immeuble ancien en fond clair"></div>
<svg class="abs" style="left:0;top:0" width="1200" height="3995" aria-hidden="true">
  <polygon points="0,806 1200,660 1200,820 0,820" fill="#fff"/>
  <polygon points="0,808 1200,636 1200,672 0,790" fill="var(--blue)"/>
  <polygon points="0,1511 1200,1350 1200,2124 0,2263" fill="var(--ice)"/>
  <polygon points="0,1511 1200,1375 1200,1350 0,1480" fill="var(--mist)"/>
  <polygon points="0,2263 1200,2124 1200,2090 0,2240" fill="var(--mist)"/>
  <polygon points="0,2990 1200,2837 1200,3650 0,3720" fill="var(--ice)"/>
  <polygon points="0,3010 1200,2860 1200,2837 0,2968" fill="var(--blue)"/>
  <polygon points="0,3720 1200,3560 1200,3995 0,3995" fill="var(--navy)"/>
  <polygon points="0,3705 1200,3540 1200,3555 0,3712" fill="#fff"/>
  <polygon points="0,3696 1200,3522 1200,3534 0,3702" fill="var(--blue)"/>
</svg>
<div class="photo" style="left:0;top:2990px;width:1200px;height:720px;background:linear-gradient(180deg,rgba(202,222,239,.2),rgba(123,173,215,.35))" role="img" aria-label="Vue pâle d'une ville avec cathédrale et bus"></div>

<!-- header -->
<div class="abs topline"></div>
<div class="abs header">
  <div class="abs logo">KELVARO</div>
  <nav class="nav">
    <a class="active" style="left:459px">Immobilier</a>
    <a style="left:604px">Services</a>
    <a style="left:710px">Calculatrice</a>
    <a style="left:854px">Contact</a>
  </nav>
  <svg class="abs" style="left:950px;top:51px" width="50" height="16" aria-hidden="true">
    <rect x="0" y="0" width="8" height="16" fill="#1a3c8c"/><rect x="8" y="0" width="8" height="16" fill="#fff"/><rect x="16" y="0" width="8" height="16" fill="#d52b1e"/>
    <polygon points="36,5 48,5 42,11" fill="#222"/>
  </svg>
  <div class="abs search"></div>
  <svg class="abs" style="left:1026px;top:50px" width="18" height="18" aria-hidden="true"><circle cx="7.5" cy="7.5" r="5" stroke="#fff" stroke-width="2" fill="none"/><line x1="11" y1="11" x2="16" y2="16" stroke="#fff" stroke-width="2"/></svg>
</div>

<!-- hero -->
<h1 class="abs display hero-title" style="color:#fff">Héritage d’un<br>bien immobilier :<br>qu’est-ce qui est<br>vraiment important ?</h1>
<div class="btn" style="left:143px;top:479px;width:167px;height:59px">Commencer</div>
<svg class="abs" style="left:562px;top:657px" width="80" height="16" aria-hidden="true">
  <circle cx="8" cy="8" r="6" fill="#fff" stroke="var(--blue)" stroke-width="3"/>
  <circle cx="28" cy="8" r="5" fill="#fff"/><circle cx="48" cy="8" r="5" fill="#fff"/><circle cx="68" cy="8" r="5" fill="#fff"/>
</svg>

<!-- immobilier -->
<svg class="abs" style="left:250px;top:902px" width="140" height="60" aria-hidden="true"><polyline points="5,60 5,5 140,5" fill="none" stroke="var(--blue)" stroke-width="4"/></svg>
<div class="photo" style="left:144px;top:959px;width:220px;height:306px;background:linear-gradient(135deg,#e6e2dc,#c9b9a6 60%,#b23a32)" role="img" aria-label="Parchemin roulé scellé à la cire rouge"></div>
<div class="photo" style="left:377px;top:866px;width:220px;height:304px;background:linear-gradient(150deg,#d9a58a,#c98b6d 45%,#6c8a3e 100%)" role="img" aria-label="Une main qui transmet une clé dorée à une autre"></div>
<h2 class="abs display" style="left:659px;top:862px;font-size:29px">Immobilier</h2>
<p class="copy" style="left:659px;top:928px;width:398px">Sed ut perspiciatis unde omnis iste natus error sit voluptatem accusantium doloremque laudantium, totam rem aperiam, eaque ipsa quae ab illo inventore veritatis et quasi architecto beatae vitae dicta sunt explicabo. Nemo enim ipsam voluptatem quia voluptas sit aspernatur aut odit aut fugit, sed quia consequuntur magni dolores eos qui ratione voluptatem seqque porro quisquam est, qui ectetur, adipisci velit, sed quia non numquam</p>
<div class="btn" style="left:660px;top:1235px;width:167px;height:58px">Read more</div>

<!-- services -->
<h2 class="abs display" style="left:0;top:1530px;width:1200px;text-align:center;font-size:29px">Services</h2>
<svg class="abs" style="left:108px;top:1906px" width="192" height="208" aria-hidden="true"><polyline points="80,2 2,2 2,206 190,206 190,120" fill="none" stroke="var(--blue)" stroke-width="4"/></svg>
<div class="photo" style="left:186px;top:1654px;width:364px;height:383px;background:linear-gradient(120deg,#8a6b45,#d8c08a 45%,#b98d4f 70%,#3d2e1e)" role="img" aria-label="Mains âgées tenant une enveloppe de documents"></div>
<h3 class="abs" style="left:608px;top:1662px;font-size:28px;font-weight:400;color:var(--ink)">Nachlassplanung</h3>
<p class="copy" style="left:608px;top:1718px;width:449px">Sed ut perspiciatis unde omnis iste natus error sit voluptatem accusantium doloremque laudantium, totam rem aperiam, eaque ipsa quae ab illo inventore veritatis et quasi architecto beatae vitae dicta sunt explicabo. Nemo enim ipsam voluptatem quia voluptas sit aspernatur aut odit aut fugit, sed quia consequuntur magni dolores eos qui ratione voluptatem seqque porro quisquam</p>
<div class="btn" style="left:609px;top:1962px;width:167px;height:58px">Read more</div>

<!-- calculatrice -->
<h2 class="abs display" style="left:146px;top:2344px;font-size:29px">Calculatrice</h2>
<p class="copy" style="left:146px;top:2409px;width:399px">Sed ut perspiciatis unde omnis iste natus error sit voluptatem accusantium doloremque laudantium, totam rem aperiam, eaque ipsa quae ab illo inventore veritatis et quasi architecto beatae vitae dicta sunt explicabo. Nemo enim ipsam voluptatem quia voluptas sit aspernatur aut odit aut fugit, sed quia consequuntur magni dolores eos qui ratione voluptatem seqque porro quisquam est, qui ectetur, adipisci velit, sed quia non numquam</p>
<div class="btn" style="left:147px;top:2719px;width:231px;height:58px">Estimer mon bien</div>
<svg class="abs" style="left:784px;top:2303px" width="272" height="204" aria-hidden="true"><polyline points="3,40 3,3 268,3 268,201 230,201" fill="none" stroke="var(--blue)" stroke-width="4"/></svg>
<div class="photo" style="left:614px;top:2345px;width:397px;height:414px;background:radial-gradient(circle at 50% 48%,#d92a2a 0 14%,#c99a86 30%,#8a6b66 70%,#5b87a8 100%)" role="img" aria-label="Mains protégeant une petite maison rouge"></div>

<!-- contact -->
<h2 class="abs display" style="left:0;top:3050px;width:1200px;text-align:center;font-size:29px">Contact us</h2>
<div class="field" style="left:233px;top:3136px;width:361px;height:55px">First Name</div>
<div class="field" style="left:605px;top:3136px;width:361px;height:55px">Last Name</div>
<div class="field" style="left:233px;top:3201px;width:361px;height:55px">Email address</div>
<div class="field" style="left:605px;top:3201px;width:361px;height:55px">Phone Number</div>
<div class="field" style="left:233px;top:3266px;width:733px;height:116px;line-height:50px">Message</div>
<div class="btn" style="left:516px;top:3412px;width:168px;height:58px">Submit</div>

<!-- footer -->
<div class="abs footer-nav"><span>IMMOBILIER</span>/<span>SERVICES</span>/<span>CALCULATRICE</span>/<span>CONTACT</span></div>
<div class="abs legal">© Copyright 2025 Companyname.All Rights Reserved &nbsp;|&nbsp; Privacy Policy &nbsp;|&nbsp; Terms of use</div>
<div class="abs social" style="left:520px" role="img" aria-label="Réseau social"></div>
<div class="abs social" style="left:577px" role="img" aria-label="Chaîne vidéo"></div>
<div class="abs social" style="left:634px" role="img" aria-label="Réseau professionnel"></div>

</body>
</html>
```